Resume: Professional Marketer seeking to impress potential recruiters with my skills & experience

Create a marketing esque style CV. I'm an outgoing, driven marketing with years of experience. I'm looking for a new senior role. My CV should look professional, but with elements of creativity and be a little bold. It should stand out amongst all the other CVs being submitted for a role. Check out my workfolio profile here: https://www.careerlinkspace.net/in/morwenna-traske-58291604/ I would like to include a photo with the design, as a subtle element of the design.

Target Market(s)

Recruiters, Headhunters

Industry/Entity Type

Marketing

Font styles to use
Sans Serif

Requirements
Must have
• Easy to read sections, with enough detail for a recruiter to understand my experience.
Nice to have
• Graphics, icons etc to represent experience

```html
<!DOCTYPE html>
<html lang="en">
<head>
<meta charset="utf-8">
<title>Curriculum Vitae – Skills and Experience</title>
<link href="https://fonts.googleapis.com/css2?family=Libre+Caslon+Text:wght@400&family=Gelasio:wght@400&display=swap" rel="stylesheet">
<style>
:root{
  --canvas:#ffffff;
  --band-light:#efe7de;
  --band-dark:#d9cabb;
  --page-right:#ddd0c3;
  --ink:#2b2622;
  --ink-soft:#3a332d;
}
*{box-sizing:border-box;margin:0;padding:0}
html,body{width:1200px;height:850px;overflow:hidden;background:var(--canvas)}
body{position:relative;font-family:"Gelasio",Georgia,serif;color:var(--ink)}
.page{position:absolute;top:12px;height:828px;overflow:hidden;box-shadow:0 0 3px rgba(0,0,0,.12)}
.page--left{left:10px;width:585px;background:var(--band-light)}
.page--right{left:606px;width:584px;background:radial-gradient(ellipse at 30% 20%,#e6dbcf 0%,var(--page-right) 55%,#d6c7b8 100%)}
.band{position:absolute;left:0;width:100%}
.band--title{background:linear-gradient(180deg,#f2ece5,var(--band-light))}
.band--skills{top:168px;height:252px;background:var(--band-dark)}
.band--roles{top:538px;height:290px;background:var(--band-dark)}
.section-title{position:absolute;left:0;width:100%;text-align:center;font-family:"Libre Caslon Text",Georgia,serif;font-size:17.5px;letter-spacing:.2px;color:var(--ink)}
.section-title--skills{top:88px}
.section-title--roles{top:470px}
.skills{position:absolute;top:183px;left:40px;display:grid;grid-template-columns:171px 171px 160px;grid-auto-rows:30.4px;list-style:none}
.skills li{font-size:10.6px;letter-spacing:.2px;color:var(--ink-soft);line-height:12.5px}
.role{position:absolute;display:grid;grid-template-columns:153px 1fr;font-size:10.4px;line-height:13.2px;color:var(--ink-soft);row-gap:0}
.role--consultant{left:40px;top:565px;width:520px}
.role--head{left:40px;top:80px;width:520px}
.role .label{grid-column:1}
.role .detail{grid-column:2}
.role p{margin-bottom:3.5px}
.gap{height:16px;grid-column:1/3}
.gap--small{height:8px;grid-column:1/3}
.steps{list-style:none;counter-reset:step}
.steps li{counter-increment:step;position:relative;padding-left:17px;margin-bottom:3.5px}
.steps li::before{content:counter(step) ".";position:absolute;left:0;width:14px;text-align:right;padding-right:3px}
.steps li:nth-child(n+10)::before{left:-4px}
</style>
</head>
<body>

<section class="page page--left">
  <div class="band band--title" style="top:0;height:168px"></div>
  <h2 class="section-title section-title--skills">KEY SKILLS AND EXPERIENCE</h2>
  <div class="band band--skills"></div>
  <ul class="skills">
    <li>ADVERTISING</li><li>DIGITAL MARKETING</li><li>MEDIA PLANNING</li>
    <li>BRANDING</li><li>DISTRIBUTION</li><li>PEOPLE MANAGEMENT</li>
    <li>BUDGETING &amp; FORECASTING</li><li>DIRECT MARKETING</li><li>PRODUCT DEVELOPMENT</li>
    <li>BUSINESS ANALYSIS</li><li>EXECUTIVE REPORTING</li><li>P&amp;L RESPONSIBILITY</li>
    <li>CALL CENTRES</li><li>FINANCIAL MODELLING</li><li>RETENTION</li>
    <li>CUSTOMER ACQUISITION</li><li>LEAD GENERATION</li><li>SALES</li>
    <li>CUSTOMER RETENTION</li><li>MARKETING ANALYSIS</li><li>STRATEGY DEVELOPMENT</li>
    <li>COPY WRITING</li><li>MARKETING</li><li style="margin-top:-7px">STAKEHOLDER<br>MANAGEMENT</li>
  </ul>
  <h2 class="section-title section-title--roles">EXPERIENCE &amp; RESPONSBILITIES FOR EACH ROLE</h2>
  <div class="band band--roles"></div>
  <div class="role role--consultant">
    <div class="label">May 2016 - May 2018</div>
    <div class="detail">Marketing Strategy Consultant</div>
    <div class="gap"></div>
    <div class="label">Role responsibilities:</div>
    <div class="detail">
      <p>Working with businesses - large and small - to drive and execute change in order to achieve their corporate and financial goals.</p>
      <p>Consulting services include; developing and improving new and existing marketing strategy, product strategy, and customer experience. Building their business and financial positions through understanding the sales process and customer path to purchase, implementing process improvement, and through improved forecasting, and cost and budget management.</p>
      <p>Primary key stakeholders are the clients management team, their teams, agencies, and suppliers.</p>
    </div>
    <div class="gap--small"></div>
    <div class="label">Reporting to:<br>Key Relationships:</div>
    <div class="detail">Clients include Spokewise, Alpenruck Re, Harlow Quay, Supper's Ready, Healthmark Private.</div>
  </div>
</section>

<section class="page page--right">
  <div class="role role--head">
    <div class="label">April 2015 - August 2015</div>
    <div class="detail">Head of Marketing<br>Meridian Cover Distribution (US) - Hearthstone Life, consumer life insurance brand</div>
    <div class="gap--small" style="height:4px"></div>
    <div class="label">Role responsibilities:</div>
    <div class="detail">
      <p>The overarching objectives of the Head of Marketing role were to:</p>
      <ol class="steps">
        <li>To prepare Hearthstone Life for the launch of the Direct Life Insurance brand.</li>
        <li>To achieve the operational new business plan (sales units, revenue &amp; appropriate acquisition expenditure), with the Head of Sales.</li>
        <li>To recruit Chief Marketing Officer to replace me (upon the planned move to Meridian Cover Distribution UK; as the role of Chief Marketing Officer, UK).</li>
      </ol>
      <p style="margin-top:6px">The objectives of the Head of Marketing:</p>
      <ol class="steps">
        <li>To develop and execute the Marketing strategy for Hearthstone Life</li>
        <li>To develop all Marketing materials for the launch, including direct response TV commercials and website</li>
        <li>To develop TV media plan and partner with a New York Media Agency</li>
        <li>To develop the Acquisition Plan to meet the Year 1 Sales unit targets, within budget</li>
        <li>To manage the marketing budget to deliver the lead, acquisition, brand, digital, and communications objectives of the organisation</li>
        <li>To take ownership of the annual acquisition budget setting process</li>
        <li>To ensure the customer retention strategy is in place to achieve the financial targets for customer retention</li>
        <li>To manage the Marketing project plan to deadline, given the critical path predominantly marketing</li>
        <li>To develop relationships and engage with all external business partners; including, Marketing Suppliers, Call Centre Operators, the Insurer and their Consultants, Printers and Mail houses, Telephony providers, Recruiters, and Legal Counsel</li>
        <li>Participate in decision making and strategic discussion for broad business planning, projects, investment decisions and strategy</li>
      </ol>
    </div>
    <div class="gap" style="height:22px"></div>
    <div class="label">Reporting to:<br>Key Relationships:</div>
    <div class="detail">
      <p>Reporting to: CEO, Meridian Cover Distribution US Key stakeholder relationships with;</p>
      <p>Five owners of Meridian Cover Distribution, Alpenruck Re US (a reinsurer), and NLMA (the insurance company).</p>
      <p>Being a start up, whilst strategic, this role was naturally ‘sleeves rolled up and hands on.’</p>
      <p>The role in the US was a 12 month contract, before a planned return to Meridian Cover Distribution (UK) as the Chief Marketing Officer. Unfortunately, this did not happen, as my husband was diagnosed with stage 4 cancer in August 2015, and died in November 2015</p>
    </div>
  </div>
</section>

</body>
</html>
```